Bright and beautiful business card for a coach

I'm a personal and business coach based in Perth, Australia. I need a business card that whilst subtle and elegant, will stand out and appeal on a table full of cards.

My business name is Tide Mentoring and the business card must represent the warmth and brightness implied in the name, without being gimmicky. It must have a warmth and appeal and be easy to read.

I prefer clean, minimalist designs.

It must align with the feel of my website and socials: https://www.tidementoring.com.au/
https://www.instagram.com/tidementoringau/
https://www.facebook.com/tidementoringau
Updates

Hi Designers Thank you so much for taking the time to submit designs. I wonder if I could have explained myself a little better. Most of the designs that have been submitted look rather formal and many have quite corporate looking embellishments on them (to my eye). I would like softer, warmer, more organic. I’m open to people playing about and being more abstract, using softer embellishments (e.g the line drawing flowers and grasses I’ve used in my socials) incorporating other colours from my palette or like the social icons in my email signature (in PDF), perhaps playing with size/oversize, playing with the bleed. Please don’t be constrained by what I’ve already done, it merely needs to compliment. I’m sorry if I’m not using the right words or have led you astray. I’m no designer, but I’ve done my website, socials, email signature etc all myself (my logo was a design contest) and I was really hoping for my business card to be something more creative than I could have made with a template. Reminder: No black cards/sides please. Thank you 😊

Target Market(s)

Individuals, most likely but not all female. Creative thinkers. Likely professionals.

Industry/Entity Type

Business & Personal Coach

Contact Information for Business Card

(Tide Mentoring Logo) Name: Maren Delsby; Title: Business & Personal Coach; Phone number: +61 (0)438 915307; Email: maren@tidementoring.com.au; Website: https://tidementoring.com.au; Social icons for Kith, Lumo & Linka: @tidementoringAU. Optional strapline: "A thinking partner to help you cut through the noise"

Font styles to use
Sans Serif

Colors
00AB8E
00BBA5
67D7C9
C6EFE9
E9F9F6
59FF00
82FF00
B8FF75
E3FFCB
F4FFEA
FFC000
F8CF3A
FAE287
FDF2CF
FEFAEE

Requirements
Must have
• Must align with feel of my website and socials. Must have a pop of #FFC000 (possibly whole of one side, or at least a block). Bright or white background. Easy to read.
Nice to have
• Possibly incorporate the sunshine/grass picture I have used in website and socials - will upload.
Should not have
• Must not be black or dark. Not impersonal or corporate looking.

```html
<!DOCTYPE html>
<html lang="en">
<head>
<meta charset="utf-8">
<title>Tide Mentoring – Business Card</title>
<link href="https://fonts.googleapis.com/css2?family=Montserrat:wght@500;600;700&display=swap" rel="stylesheet">
<style>
  :root {
    --sun-yellow: #F8C22B;
    --amber: #C5761D;
    --pale-yellow: #FDE994;
    --slate: #627272;
    --teal: #159A8E;
    --teal-badge: #179A8F;
    --gold-badge: #C08A08;
    --bright-yellow: #FFC000;
    --white: #FFFFFF;
  }
  html, body {
    margin: 0;
    padding: 0;
    overflow: hidden;
    background: var(--white);
  }
  .card {
    position: relative;
    width: 1200px;
    height: 686px;
    overflow: hidden;
    background: var(--white);
    font-family: 'Montserrat', sans-serif;
  }
  .card-art {
    position: absolute;
    inset: 0;
  }
  .line-pattern {
    position: absolute;
    left: 0;
    top: 0;
    width: 460px;
    height: 230px;
    background: linear-gradient(160deg, #F2B628 0%, var(--sun-yellow) 85%);
    border-bottom-right-radius: 100% 100%;
  }
  .sun-ornament {
    position: absolute;
    left: 455px;
    top: 535px;
    width: 96px;
    height: 96px;
    border-radius: 50%;
    background: radial-gradient(circle, var(--amber) 0%, var(--amber) 35%, #DC9A24 70%, var(--sun-yellow) 100%);
  }
  .brand-name {
    position: absolute;
    left: 90px;
    top: 330px;
    width: 360px;
    text-align: center;
    margin: 0;
    color: var(--white);
    font-weight: 600;
    font-size: 38px;
    letter-spacing: 1px;
  }
  .identity {
    position: absolute;
    left: 668px;
    top: 152px;
  }
  .person-name {
    margin: 0;
    color: var(--slate);
    font-weight: 700;
    font-size: 53px;
    line-height: 1;
    letter-spacing: 0.5px;
  }
  .person-title {
    margin: 14px 0 0 2px;
    color: var(--slate);
    font-weight: 600;
    font-size: 27px;
  }
  .contact-list {
    position: absolute;
    left: 670px;
    top: 398px;
    margin: 0;
    padding: 0;
    list-style: none;
  }
  .contact-item {
    display: flex;
    align-items: center;
    height: 44px;
    margin-bottom: 12px;
    color: var(--slate);
    font-weight: 500;
    font-size: 24px;
  }
  .contact-icon {
    width: 44px;
    height: 40px;
    margin-right: 13px;
    flex: none;
  }
  .social-row {
    position: absolute;
    left: 672px;
    top: 596px;
    height: 40px;
    display: flex;
    align-items: center;
  }
  .social-network {
    display: flex;
    align-items: center;
    margin-right: 12px;
    color: var(--slate);
    font-weight: 500;
    font-size: 17px;
  }
  .social-dot {
    width: 24px;
    height: 24px;
    border-radius: 50%;
    margin-right: 6px;
    flex: none;
  }
  .social-dot--gold { background: var(--gold-badge); }
  .social-dot--yellow { background: var(--bright-yellow); }
  .social-dot--teal { background: var(--teal-badge); }
  .social-divider {
    width: 5px;
    height: 38px;
    background: var(--slate);
    margin: 0 10px 0 2px;
  }
  .social-handle {
    color: var(--teal);
    font-weight: 500;
    font-size: 24px;
  }
</style>
</head>
<body>
<main class="card">
  <svg class="card-art" width="1200" height="686" viewBox="0 0 1200 686" aria-hidden="true">
    <path fill="var(--amber)" d="M733 0 C760 45 800 70 880 82 C930 90 960 92 990 98 C1040 110 1090 140 1133 162 C1160 174 1185 178 1200 182 L1200 0 Z"/>
    <circle fill="var(--pale-yellow)" cx="1158" cy="289" r="53"/>
    <circle fill="var(--pale-yellow)" cx="920" cy="404" r="53"/>
    <circle fill="var(--pale-yellow)" cx="1158" cy="595" r="205"/>
    <circle fill="var(--pale-yellow)" cx="861" cy="662" r="53"/>
    <path fill="var(--sun-yellow)" d="M0 0 L598 0 C575 70 563 150 566 240 C569 330 590 380 598 430 C608 480 604 560 586 686 L0 686 Z"/>
    <path fill="var(--amber)" d="M0 534 C50 536 90 542 110 553 C170 585 210 618 270 615 C320 612 370 650 404 686 L0 686 Z"/>
  </svg>

  <div class="line-pattern" role="img" aria-label="Flowing amber line pattern"></div>
  <div class="sun-ornament" role="img" aria-label="Small amber sun ornament"></div>

  <p class="brand-name">Tide Mentoring</p>

  <section class="identity">
    <h1 class="person-name">MAREN DELSBY</h1>
    <p class="person-title">Business &amp; Personal Coach</p>
  </section>

  <ul class="contact-list">
    <li class="contact-item">
      <svg class="contact-icon" viewBox="0 0 44 40" aria-hidden="true">
        <path fill="var(--slate)" d="M4 4 C6 1 11 1 12 3 L15 11 C16 13 14 15 12 16 C14 22 18 26 24 29 C25 27 27 25 29 26 L35 30 C37 32 35 37 32 38 C18 38 2 22 2 10 C2 8 3 5 4 4 Z"/>
      </svg>
      +61 (0)438 915307
    </li>
    <li class="contact-item">
      <svg class="contact-icon" viewBox="0 0 44 40" aria-hidden="true">
        <rect x="1" y="5" width="42" height="30" fill="var(--slate)"/>
        <path d="M3 7 L22 23 L41 7 M3 33 L17 20 M41 33 L27 20" fill="none" stroke="var(--white)" stroke-width="2.5"/>
      </svg>
      maren@tidementoring.com.au
    </li>
    <li class="contact-item">
      <svg class="contact-icon" viewBox="0 0 44 40" aria-hidden="true">
        <circle cx="22" cy="20" r="20" fill="var(--slate)"/>
        <g fill="none" stroke="var(--white)" stroke-width="2.5">
          <ellipse cx="22" cy="20" rx="9" ry="20"/>
          <path d="M2 13 H42 M2 27 H42 M22 0 V40"/>
        </g>
      </svg>
      https://tidementoring.com.au
    </li>
  </ul>

  <div class="social-row">
    <span class="social-network"><span class="social-dot social-dot--gold"></span>Lumo</span>
    <span class="social-network"><span class="social-dot social-dot--yellow"></span>Kith</span>
    <span class="social-network"><span class="social-dot social-dot--teal"></span>Linka</span>
    <span class="social-divider"></span>
    <span class="social-handle">@TideMentoringAU</span>
  </div>
</main>
</body>
</html>
```